New furniture company needs a cool, fresh Website - think lounjo.com, velmora.com

Tuftwell.com: We are launching a home (Storvane) furniture business, aimed at the young, discerning mid-market consumer. The aim is to compete with many furniture e-tailers, as well as more established retail brands.
We want the website to capture the hearts, minds and wallets of the target audience, placing Tuftwell.com firmly into the market place. Please look to Velmora.com for look and feel inspiration. We will be selling approx 15 products to start. I suggest using Storvane with the following theme please: – Hearth & Meadow – Radiance – Belmont. Please see the logo below. The website needs to have a sophisticated feel for affordable aspirational furniture. Soft colours and homely text - please go with look and feel of Velmora.com. Please see a below file containing image of some sofas, chairs and footstools that will be for sale.
Many thanks

Target Market(s)

mid-market, young families looking for cool, affordable, easy to buy furniture

Industry/Entity Type

Furniture

Coding

Coded - Design and coding required

Number of Pages Required

5+ page

Font styles to use
Sans Serif

Colors
86cae7
cee9f5
3277b5
eaf2ce
fdf9ce
fff3d1
0255a3
e8e8e8
cbcbcb

Requirements
Must have
• Storvane
• http://www.velmora.com/hartwick-leather-large-sofa.html - great example of what we need it to look like
• logo as shown
• homepage
• products menu - sofas, seating, footstools, antique
• images of all products (examples provided) with ability to click on various fabric swatch samples and see the sofa in different fabrics and colours (check out lounjo.com)
• facility for social media
• facility to buy online
• "add to wishlist"
• "add to basket"
Nice to have
• I want it to have a light and airy feel, nothing too heavy or corporate. Needs to be very easily navigated and a simple approach
Should not have
• Dark, heavy colours

```html
<!DOCTYPE html>
<html lang="en">
<head>
<meta charset="utf-8">
<title>Tuftwell – Categories</title>
<link href="https://fonts.googleapis.com/css2?family=Roboto:wght@300;400;500;700&display=swap" rel="stylesheet">
<style>
:root{
  --sky:#86cae7;
  --sky-pale:#cee9f5;
  --blue:#3277b5;
  --navy:#0255a3;
  --grey-light:#e8e8e8;
  --grey-mid:#cbcbcb;
  --band:#7f9db1;
  --ink:#333;
  --muted:#888;
  --dark:#2b2b2b;
  --darker:#222;
  --white:#fff;
}
*{box-sizing:border-box;margin:0;padding:0}
html,body{width:741px;height:1200px;overflow:hidden}
body{font-family:'Roboto',sans-serif;color:var(--ink);background:var(--white);font-size:8px;position:relative}
ul{list-style:none}

/* header */
.site-header{height:86px;position:relative;border-bottom:1px solid var(--grey-light)}
.social{position:absolute;left:30px;top:14px;display:flex;gap:6px}
.social span{width:15px;height:15px;border-radius:50%;background:var(--grey-mid);display:block}
.social span:first-child{background:var(--band)}
.brand{position:absolute;left:50%;top:8px;transform:translateX(-50%);text-align:center}
.brand .mark{width:18px;height:18px;border-radius:50%;border:1px solid var(--muted);margin:0 auto 3px}
.brand .name{font-size:13px;letter-spacing:3px;font-weight:400;color:var(--muted)}
.header-tools{position:absolute;right:30px;top:12px;display:flex;gap:22px}
.tool{text-align:center;font-size:6px;color:var(--muted)}
.tool svg{display:block;margin:0 auto 2px}
.main-nav{position:absolute;top:62px;left:0;right:0;display:flex;justify-content:center;gap:16px;font-size:7px;font-weight:500;color:#555;align-items:center}

/* title band */
.page-title{height:42px;background:var(--grey-light);display:flex;align-items:center;justify-content:space-between;padding:0 52px}
.page-title h1{font-size:15px;font-weight:700;color:#444}
.crumbs{font-size:7px;color:var(--muted)}
.crumbs b{color:#555;font-weight:500}

/* content */
.content{display:flex;padding:0 40px 0 50px;height:690px}
.sidebar{width:152px;padding-top:22px;border-right:1px solid var(--grey-light);padding-right:14px}
.filter{margin-bottom:18px}
.filter h3{font-size:7px;font-weight:700;color:#444;margin-bottom:7px;display:flex;justify-content:space-between}
.filter li{font-size:6.5px;color:var(--muted);margin:0 0 5px 6px;display:flex;align-items:center;gap:4px}
.dot{width:6px;height:6px;border-radius:50%;border:1px solid var(--grey-mid)}
.dot.on{background:var(--blue);border-color:var(--blue)}
.range{position:relative;height:14px;margin-top:6px}
.range .track{position:absolute;left:6px;right:0;top:6px;height:2px;background:var(--grey-mid)}
.range .fill{position:absolute;left:20px;right:40px;top:6px;height:2px;background:var(--blue)}
.range .knob{position:absolute;top:2px;width:9px;height:9px;border-radius:50%;background:var(--blue)}
.range-vals{display:flex;justify-content:space-between;font-size:6px;color:var(--muted);margin:0 0 0 6px}
.stars{color:#f0b429;letter-spacing:1px;font-size:7px}

.grid{flex:1;display:grid;grid-template-columns:repeat(3,1fr);gap:14px 14px;padding:26px 0 0 18px;align-content:start}
.card{height:206px;text-align:center}
.card .photo{height:148px;background:linear-gradient(#f7f7f7,#ececec);border:1px solid var(--grey-light);position:relative}
.card .photo .sofa{position:absolute;left:18%;right:18%;top:38%;height:28%;border-radius:6px;background:linear-gradient(#9a9aa5,#6c6c78)}
.card.hover .photo{background:linear-gradient(#a6a6ae,#8c8c96)}
.badge{position:absolute;left:0;top:0;background:var(--sky);color:#fff;font-size:6px;padding:3px 5px;font-weight:700}
.quick{width:16px;height:16px;border-radius:50%;background:var(--white);border:1px solid var(--grey-light);margin:-8px auto 0;position:relative}
.card.hover .quick{background:var(--sky);border-color:var(--sky)}
.card h4{font-size:7px;font-weight:700;margin-top:10px;color:#444}
.card .price{font-size:6.5px;color:var(--blue);margin-top:4px}

.pager{display:flex;justify-content:center;gap:6px;margin-top:-28px;padding-left:190px}
.pager span{width:15px;height:15px;border-radius:50%;border:1px solid var(--grey-mid);font-size:6px;display:flex;align-items:center;justify-content:center;color:var(--muted)}
.pager .on{background:var(--blue);border-color:var(--blue);color:#fff}

/* features band */
.features{position:absolute;top:904px;left:0;right:0;height:60px;background:var(--band);display:flex;justify-content:space-around;color:#fff;font-size:7px;font-weight:700;align-items:center}
.features div{text-align:center}
.features svg{display:block;margin:0 auto 4px}

/* newsletter */
.newsletter{position:absolute;top:975px;left:0;right:0;height:50px;background:var(--dark);display:flex;align-items:center;padding:0 52px;color:#fff}
.newsletter h2{font-size:11px;font-weight:400;flex:1;letter-spacing:.5px}
.newsletter .field{width:265px;height:18px;background:#3a3a3a;font-size:6px;color:#999;padding:5px 8px}
.newsletter .btn{height:18px;background:#fff;color:#333;font-size:6px;font-weight:700;padding:5px 10px}

/* footer */
.site-footer{position:absolute;top:1025px;left:0;right:0;height:175px;background:var(--dark);color:#aaa}
.cols{display:flex;padding:22px 52px 0;gap:20px}
.col{flex:1;font-size:6px}
.col h5{color:#fff;font-size:7px;font-weight:700;margin-bottom:8px}
.col li{margin-bottom:4px}
.contact li{display:flex;gap:4px}
.contact .ico{width:5px;height:5px;border-radius:50%;background:var(--sky);margin-top:1px;flex:none}
.foot-social{display:flex;gap:4px;margin-top:6px}
.foot-social span{width:9px;height:9px;border-radius:50%;background:#555}
.copyright{position:absolute;bottom:0;left:0;right:0;height:28px;background:var(--darker);display:flex;align-items:center;justify-content:space-between;padding:0 52px;font-size:6px}
.cards{display:flex;gap:3px}
.cards span{width:16px;height:10px;background:#666;border-radius:1px}
.to-top{position:absolute;right:14px;bottom:8px;width:14px;height:14px;border-radius:50%;background:#fff}
</style>
</head>
<body>
<header class="site-header">
  <div class="social"><span></span><span></span><span></span><span></span><span></span></div>
  <div class="brand"><div class="mark"></div><div class="name">TUFTWELL</div></div>
  <div class="header-tools">
    <div class="tool"><svg width="12" height="12" viewBox="0 0 12 12" fill="none" stroke="#888"><path d="M1 2h2l2 6h5l1-4H4"/><circle cx="5.5" cy="10" r="1"/><circle cx="9.5" cy="10" r="1"/></svg>Cart</div>
    <div class="tool"><svg width="12" height="12" viewBox="0 0 12 12" fill="none" stroke="#888"><path d="M6 10.5 1.5 6A2.5 2.5 0 0 1 6 3a2.5 2.5 0 0 1 4.5 3z"/></svg>Wishlist</div>
    <div class="tool"><svg width="12" height="12" viewBox="0 0 12 12" fill="none" stroke="#888"><circle cx="6" cy="4" r="2.5"/><path d="M1.5 11a4.5 4.5 0 0 1 9 0"/></svg>Account</div>
  </div>
  <nav class="main-nav"><span>HOME</span><span>SOFAS</span><span>SEATING</span><span>FOOTSTOOLS</span><span>ANTIQUE</span>
    <svg width="8" height="8" viewBox="0 0 8 8" fill="none" stroke="#555"><circle cx="3.3" cy="3.3" r="2.5"/><path d="M5.2 5.2 7.5 7.5"/></svg></nav>
</header>

<section class="page-title"><h1>CATEGORIES</h1><div class="crumbs"><b>HOME</b> &nbsp;/&nbsp; CATEGORY</div></section>

<main class="content">
  <aside class="sidebar">
    <div class="filter"><h3>Categories <span>–</span></h3>
      <ul><li><span class="dot on"></span>Sofas</li><li><span class="dot"></span>Seating</li><li><span class="dot"></span>Footstools</li><li><span class="dot"></span>Antique</li></ul></div>
    <div class="filter"><h3>Filters <span>+</span></h3>
      <h3>Availability</h3>
      <ul><li><span class="dot on"></span>In stock (12)</li><li><span class="dot"></span>Out of stock (3)</li></ul></div>
    <div class="filter"><h3>Price <span>+</span></h3>
      <div class="range-vals"><span>£400</span><span>£2000</span></div>
      <div class="range"><div class="track"></div><div class="fill"></div><div class="knob" style="left:16px"></div><div class="knob" style="right:36px"></div></div></div>
    <div class="filter"><h3>Rating <span>+</span></h3>
      <ul><li><span class="dot on"></span>All</li><li><span class="dot"></span><span class="stars">★★★★★</span></li><li><span class="dot"></span><span class="stars">★★★★☆</span></li><li><span class="dot"></span><span class="stars">★★★☆☆</span></li><li><span class="dot"></span><span class="stars">★★☆☆☆</span></li></ul></div>
  </aside>

  <div class="grid">
    <article class="card"><div class="photo" role="img" aria-label="Grey patterned three-seat sofa"><div class="sofa"></div></div><div class="quick"></div><h4>PRODUCT NAME HERE</h4><p class="price">£1,020.00</p></article>
    <article class="card hover"><div class="photo" role="img" aria-label="Sofa with wishlist and basket options shown"><span class="badge">NEW</span></div><div class="quick"></div><h4>PRODUCT NAME HERE</h4><p class="price">£1,020.00</p></article>
    <article class="card"><div class="photo" role="img" aria-label="Cream tufted sofa"><div class="sofa" style="background:linear-gradient(#eee,#d8d8d8)"></div></div><div class="quick"></div><h4>PRODUCT NAME HERE</h4><p class="price">£1,020.00</p></article>
    <article class="card"><div class="photo" role="img" aria-label="Beige fabric sofa"><div class="sofa" style="background:linear-gradient(#d9c2a5,#b89b7a)"></div></div><div class="quick"></div><h4>PRODUCT NAME HERE</h4><p class="price">£1,020.00</p></article>
    <article class="card"><div class="photo" role="img" aria-label="Grey modern sofa"><div class="sofa" style="background:linear-gradient(#b4b4b4,#8e8e8e)"></div></div><div class="quick"></div><h4>PRODUCT NAME HERE</h4><p class="price">£1,020.00</p></article>
    <article class="card"><div class="photo" role="img" aria-label="Black leather sofa"><div class="sofa" style="background:linear-gradient(#444,#1e1e1e)"></div></div><div class="quick"></div><h4>PRODUCT NAME HERE</h4><p class="price">£1,020.00</p></article>
    <article class="card"><div class="photo" role="img" aria-label="Black chaise longue"><div class="sofa" style="background:linear-gradient(#3c3c3c,#1c1c1c)"></div></div><div class="quick"></div><h4>PRODUCT NAME HERE</h4><p class="price">£1,020.00</p></article>
    <article class="card"><div class="photo" role="img" aria-label="Taupe buttoned armchair"><div class="sofa" style="background:linear-gradient(#c9b9a6,#9d8c78)"></div></div><div class="quick"></div><h4>PRODUCT NAME HERE</h4><p class="price">£1,020.00</p></article>
    <article class="card"><div class="photo" role="img" aria-label="White corner sofa"><div class="sofa" style="background:linear-gradient(#f4f4f4,#dcdcdc)"></div></div><div class="quick"></div><h4>PRODUCT NAME HERE</h4><p class="price">£1,020.00</p></article>
  </div>
</main>

<nav class="pager"><span>«</span><span>1</span><span>2</span><span class="on">3</span><span>4</span><span>5</span><span>…</span><span>10</span><span>»</span></nav>

<section class="features">
  <div><svg width="18" height="14" viewBox="0 0 18 14" fill="none" stroke="#fff"><circle cx="7" cy="7" r="6"/><path d="M1 7h12M7 1c3 3 3 9 0 12M7 1c-3 3-3 9 0 12"/></svg>WORLDWIDE SHIPPING</div>
  <div><svg width="18" height="14" viewBox="0 0 18 14" fill="none" stroke="#fff"><path d="M1 3h10v7H1zM11 6h4l2 2v2h-6"/><circle cx="4" cy="11" r="1.5"/><circle cx="14" cy="11" r="1.5"/></svg>FLAT SHIPPING PER ITEM</div>
  <div><svg width="18" height="14" viewBox="0 0 18 14" fill="none" stroke="#fff"><circle cx="9" cy="7" r="6"/><path d="M9 3v8M7 5h3a1 1 0 0 1 0 2H8a1 1 0 0 0 0 2h3"/></svg>MONEY BACK GUARANTEE</div>
  <div><svg width="18" height="14" viewBox="0 0 18 14" fill="none" stroke="#fff"><path d="M3 5a6 6 0 1 1 0 4M3 1v4h4"/></svg>EASY RETURNS</div>
</section>

<section class="newsletter">
  <h2>SUBSCRIBE TO OUR NEWSLETTER</h2>
  <div class="field">Enter your email address...</div><div class="btn">SUBSCRIBE</div>
</section>

<footer class="site-footer">
  <div class="cols">
    <div class="col"><h5>MY ACCOUNT</h5><ul><li>My Account</li><li>Order History</li><li>Returns</li><li>Advanced Search</li><li>Download Service</li></ul></div>
    <div class="col"><h5>CUSTOMER SERVICE</h5><ul><li>Sitemap</li><li>Privacy Policy</li><li>Your Account</li><li>Advanced Search</li><li>Contact Us</li></ul></div>
    <div class="col"><h5>OUR SERVICE</h5><ul><li>My Account</li><li>Order History</li><li>Returns</li><li>Specials</li><li>About Us</li></ul></div>
    <div class="col contact"><h5>CONTACT US</h5><ul><li><span class="ico"></span>14 Linden Row, Harbourside, Bristol BS1 4QP</li><li><span class="ico"></span>Call us now: +44 (0) 20 7946 0321</li><li><span class="ico"></span>hello@tuftwell.com</li></ul>
      <div class="foot-social"><span></span><span></span><span></span><span></span><span></span></div></div>
  </div>
  <div class="copyright"><span>Copyright 2017 | All Right Reserved</span><div class="cards"><span></span><span></span><span></span><span></span><span></span></div></div>
  <div class="to-top"></div>
</footer>
</body>
</html>
```